Industrial automation company needs new business cards

We need a new business card designed. We have an existing logo that is very simple and are happy to consider changes to it. We have been in business for more than 10 years and our logo has some brand recognition.
We are a company of engineers and build systems for industrial automation, substation automation, power and energy monitoring and production data vertical integration. Our main clients are food manufacturers, data centers and government establishments.
Our current business cards have our name, qualifications, job title, telephone, email and web address details. We don't need our physical address on our business cards. I've attached our current logo

Industry/Entity Type

Business

Logo Text

vardo

Font styles to use
Sans Serif

Colors
6b449b

Requirements
Must have
• - double sided business cards
• - name (eg Mara Quill)
• - qualifications (BE Elec MAGSO)
• - job title (eg Senior Engineer)
• - telephone (eg 0472 518 396)
• - email (eg mara.quill@vardo.com.au)
• - web address (eg vardo.com.au)
Nice to have
• include our target markets on the back side of the card
• - industrial automation
• - substation automation
• - power and energy monitoring
• - production data vertical integration

```html
<!DOCTYPE html>
<html lang="en">
<head>
<meta charset="utf-8">
<title>Vardo business card</title>
<link href="https://fonts.googleapis.com/css2?family=Orbitron:wght@700&family=Oswald:wght@300;600&family=Raleway:wght@500&display=swap" rel="stylesheet">
<style>
  :root {
    --violet-1: #9a6fdc;
    --violet-2: #7d5cb4;
    --violet-3: #6b449b;
    --violet-4: #57417f;
    --violet-5: #422a6c;
    --edge: #4a2e72;
    --card-grey: #c9c9c9;
    --card-light: #ececec;
    --white: #ffffff;
  }
  * { margin: 0; padding: 0; box-sizing: border-box; }
  html, body { width: 1200px; height: 1000px; overflow: hidden; }
  body {
    position: relative;
    background: radial-gradient(ellipse at 50% 45%, #ffffff 0%, #f2f2f2 55%, #dcdcdc 100%);
    font-family: "Raleway", sans-serif;
  }
  .card {
    position: absolute;
    border: 4px solid var(--edge);
    box-shadow: 6px 8px 10px rgba(0,0,0,0.35);
    overflow: hidden;
  }
  .card--front {
    left: 212px; top: 72px; width: 678px; height: 391px;
    background: radial-gradient(circle at 50% 48%, var(--card-light) 0%, #d6d6d6 45%, #bdbdbd 100%);
  }
  .card--back {
    left: 225px; top: 551px; width: 679px; height: 390px;
    background: radial-gradient(circle at 50% 50%, var(--card-light) 0%, #cfcfcf 50%, #b8b8b8 100%);
  }
  .pattern {
    position: absolute;
    background: linear-gradient(160deg, var(--violet-4) 0%, var(--violet-2) 45%, var(--violet-1) 70%, var(--violet-4) 100%);
    opacity: 0.85;
  }
  .card--front .pattern { left: 42px; top: 0; width: 320px; height: 387px;
    clip-path: polygon(12% 0, 62% 0, 100% 78%, 85% 100%, 55% 100%, 20% 60%, 0 25%); }
  .markets { position: absolute; left: 8px; top: 214px; width: 160px; list-style: none; }
  .markets li {
    font-family: "Orbitron", sans-serif; font-weight: 700; font-size: 10.5px;
    color: var(--white); text-align: center; line-height: 13px;
    text-shadow: 0 0 2px #333, 0 0 1px #000;
    padding-bottom: 5px; margin-bottom: 8px;
    border-bottom: 4px solid var(--violet-5);
  }
  .markets li:last-child { border-bottom: none; }
  .brand {
    position: absolute; left: 440px; top: 254px;
    display: flex; align-items: center; gap: 10px;
    font-family: "Orbitron", sans-serif; font-weight: 700; font-size: 30px;
    color: var(--violet-4); letter-spacing: 1px;
  }
  .brand__dot { width: 14px; height: 14px; border-radius: 50%; background: var(--violet-3); }
  .band-line { position: absolute; left: 0; width: 100%; height: 3px; background: var(--edge); }
  .pattern--top { left: 22px; top: 0; width: 220px; height: 106px;
    clip-path: polygon(0 0, 100% 0, 80% 100%, 30% 100%); }
  .pattern--bottom { left: 474px; top: 276px; width: 180px; height: 110px;
    clip-path: polygon(20% 0, 100% 0, 95% 100%, 30% 100%, 0 55%); }
  .band {
    position: absolute; left: 0; top: 112px; width: 100%; height: 165px;
    background: radial-gradient(ellipse at 48% 50%, var(--violet-1) 0%, var(--violet-3) 45%, var(--violet-5) 100%);
    border-bottom: 4px solid #d9d9d9;
  }
  .identity { position: absolute; right: 432px; top: 16px; text-align: right; color: var(--white); }
  .identity__name { font-family: "Oswald", sans-serif; font-weight: 600; font-size: 40px; line-height: 48px; text-shadow: 2px 3px 4px rgba(0,0,0,0.5); }
  .identity__title { font-family: "Oswald", sans-serif; font-weight: 300; font-size: 27px; line-height: 40px; }
  .identity__quals { font-family: "Oswald", sans-serif; font-weight: 300; font-size: 14px; margin-top: 6px; }
  .divider { position: absolute; left: 288px; top: 12px; width: 8px; height: 133px; border-radius: 4px; background: var(--white); }
  .contacts { position: absolute; left: 340px; top: 10px; list-style: none; }
  .contacts li { display: flex; align-items: center; height: 40px; margin-bottom: 9px; color: var(--white); font-size: 16px; letter-spacing: 0.5px; text-shadow: 1px 2px 3px rgba(0,0,0,0.45); }
  .contacts svg { width: 57px; height: 40px; margin-right: 8px; flex: none; }
  .swatches { position: absolute; left: 1004px; top: 386px; width: 74px; }
  .swatch { display: block; margin-bottom: 2px; }
</style>
</head>
<body>
  <section class="card card--front">
    <div class="pattern" role="img" aria-label="Scattered violet triangle pattern"></div>
    <ul class="markets">
      <li>INDUSTRIAL<br>AUTOMATION</li>
      <li>SUBSTATION<br>AUTOMATION</li>
      <li>PRODUCTION DATA<br>VERTICAL INTEGRATION</li>
      <li>POWER AND ENERGY<br>MONITORING</li>
    </ul>
    <div class="brand"><span class="brand__dot"></span><span>VARDO</span></div>
  </section>

  <section class="card card--back">
    <div class="pattern pattern--top" role="img" aria-label="Violet triangle pattern"></div>
    <div class="band-line" style="top:102px"></div>
    <div class="band">
      <div class="identity">
        <div class="identity__name">MARA QUILL</div>
        <div class="identity__title">SENIOR ENGINEER</div>
        <div class="identity__quals">(BE ELEC., MAGSO)</div>
      </div>
      <div class="divider"></div>
      <ul class="contacts">
        <li>
          <svg viewBox="0 0 57 40"><rect x="1" y="1" width="55" height="38" fill="none" stroke="#fff" stroke-width="1.5"/><rect x="16" y="11" width="25" height="17" fill="#fff"/><path d="M16 11 L28.5 21 L41 11" fill="none" stroke="#6b449b" stroke-width="1.5"/></svg>
          mara.quill@vardo.com.au
        </li>
        <li>
          <svg viewBox="0 0 57 40"><rect x="1" y="1" width="55" height="38" fill="none" stroke="#fff" stroke-width="1.5"/><path d="M28.5 8 L42 20 L38 20 L38 32 L31 32 L31 25 L26 25 L26 32 L19 32 L19 20 L15 20 Z" fill="#fff"/></svg>
          vardo.com.au
        </li>
        <li>
          <svg viewBox="0 0 57 40"><rect x="1" y="1" width="55" height="38" fill="none" stroke="#fff" stroke-width="1.5"/><path d="M21 9 L25 8 L28 15 L25 17 Q27 23 32 27 L35 24 L41 28 L39 32 Q33 34 26 27 Q20 20 21 9 Z" fill="#fff"/></svg>
          0472 518 396
        </li>
      </ul>
    </div>
    <div class="band-line" style="top:283px"></div>
    <div class="pattern pattern--bottom" role="img" aria-label="Violet triangle pattern"></div>
  </section>

  <div class="swatches" aria-hidden="true">
    <span class="swatch" style="height:70px;background:var(--violet-1)"></span>
    <span class="swatch" style="height:36px;background:var(--violet-2)"></span>
    <span class="swatch" style="height:31px;background:var(--violet-3)"></span>
    <span class="swatch" style="height:31px;background:var(--violet-4)"></span>
    <span class="swatch" style="height:50px;margin-left:-2px;width:78px;background:var(--violet-5)"></span>
  </div>
</body>
</html>
```